Flyer Design Project

We want to design a flyer for a laundromat in San Francisco. It will be used to market the services of the laundromat. I am uploading a .jpg file with details to be highlighted. The flyer should be of size 8.5 in x 11 in and should be attractive and hard hitting. The attachment should only be used for the copy, not for design.

Target Market(s)

Laundromat and laundry users

Requirements
Must have
• Must have a attention grabbing headline
Nice to have
• Pictures

```html
<!DOCTYPE html>
<html lang="en">
<head>
<meta charset="utf-8">
<title>Bayline Laundromat Flyer</title>
<link rel="stylesheet" href="https://fonts.googleapis.com/css2?family=Roboto+Condensed:wght@400;700&family=Cormorant+Garamond:wght@500&display=swap">
<style>
:root{
  --stage:#ececec;
  --navy:#0e1d66;
  --royal:#1c3aa6;
  --sky:#2e8fe0;
  --aqua:#9fd8f7;
  --foam:#e4f5fd;
  --title-blue:#1867c4;
  --ink:#1d1d1d;
  --white:#ffffff;
  --red:#e3202a;
  --lime:#8cc63f;
  --ring-green:#2f8f3a;
}
*{box-sizing:border-box;margin:0;padding:0}
html,body{width:1200px;height:917px;overflow:hidden}
body{background:var(--stage);position:relative;font-family:"Roboto Condensed",Arial,sans-serif}
.flyer{position:absolute;top:110px;width:540px;height:700px;overflow:hidden;
  background:linear-gradient(160deg,var(--royal) 0%,#2457c4 45%,var(--sky) 75%,#1b47b3 100%);
  box-shadow:0 4px 12px rgba(0,0,0,.25)}
.flyer--front{left:48px}
.flyer--back{left:614px}
.flyer__sweep{position:absolute;inset:0;width:100%;height:100%}
.header-band{position:absolute;left:0;top:0;width:540px;height:210px}
.brand{position:absolute;display:flex;align-items:center;gap:12px}
.brand__mark{width:70px;height:70px;border-radius:50%;background:#c9ced6;border:4px solid #e9edf2;flex:none}
.brand__name{font-family:"Cormorant Garamond",Georgia,serif;font-weight:500;color:var(--white);font-size:31px;line-height:1}
.photo{position:absolute;border-radius:50%;box-shadow:0 0 0 7px var(--navy),-7px 5px 0 10px var(--ring-green)}
.photo--couple{left:298px;top:-4px;width:238px;height:238px;
  background:radial-gradient(circle at 45% 55%,#f0c9a8 0%,#c98a4e 30%,#8aa3b6 60%,#dfe6ec 100%)}
.photo--towels{left:275px;top:392px;width:280px;height:280px;
  background:radial-gradient(circle at 45% 60%,#f3e3a0 0%,#c9d98a 30%,#7a8a99 60%,#cfd7de 100%)}
.photo--washer{left:238px;top:175px;width:302px;height:392px;
  background:linear-gradient(180deg,rgba(200,225,245,0) 0%,#9fbfdc 35%,#6f92b5 70%,rgba(60,110,190,0) 100%)}
.headline{position:absolute;left:26px;top:220px;color:var(--white);font-weight:700;font-size:27px;line-height:1.1;text-transform:uppercase}
.burst{position:absolute}
.burst svg{position:absolute;inset:0;width:100%;height:100%}
.burst__text{position:relative;height:100%;display:flex;flex-direction:column;align-items:center;justify-content:center;text-align:center;color:var(--white);text-transform:uppercase;font-weight:700}
.burst--offer{left:407px;top:237px;width:128px;height:128px}
.burst--offer .burst__big{font-size:21px;line-height:1}
.burst--offer .burst__small{font-size:7.5px;line-height:1.25;margin-top:3px}
.burst--contact{left:272px;top:516px;width:278px;height:190px}
.burst--contact .burst__text{color:var(--navy);padding-top:22px}
.burst--contact .burst__title{font-size:14px}
.burst--contact .burst__line{font-size:9px;line-height:1.35;font-weight:700}
.burst--contact .burst__phone{font-size:19px;line-height:1.2}
.bubble{position:absolute;border-radius:50%;
  background:radial-gradient(circle at 50% 42%,var(--white) 58%,#e2ebf6 80%,#b5c9e4 100%);
  box-shadow:0 0 0 6px var(--navy),-7px 5px 0 10px var(--ring-green),0 0 0 14px rgba(20,40,120,.35);
  display:flex;flex-direction:column;align-items:center;justify-content:center;text-align:center;padding:0 18px;text-transform:uppercase}
.bubble__title{color:var(--title-blue);font-weight:700;font-size:17px;line-height:1.08}
.bubble__body{color:var(--ink);font-weight:700;font-size:8px;line-height:1.35;margin-top:5px}
.bubble__title--red{color:var(--red);font-size:27px}
.bubble__body--large{font-size:12px;line-height:1.25}
.call{position:absolute;right:18px;top:610px;color:var(--white);text-align:right;font-weight:700;line-height:1.05;text-shadow:0 1px 3px rgba(0,0,0,.4)}
.call__label{font-size:22px}
.call__phone{font-size:25px}
</style>
</head>
<body>

<section class="flyer flyer--front" aria-label="Flyer front">
  <svg class="flyer__sweep" viewBox="0 0 540 700" aria-hidden="true">
    <path d="M0 380 C160 300 320 330 540 250 L540 700 L0 700 Z" fill="#2c7fd9" opacity=".45"/>
    <path d="M60 700 C200 560 380 520 540 420 L540 700 Z" fill="#36a0ea" opacity=".35"/>
  </svg>
  <svg class="header-band" viewBox="0 0 540 210" aria-hidden="true">
    <rect width="540" height="120" fill="var(--navy)"/>
    <path d="M0 120 C90 80 200 140 300 105 C390 75 470 110 540 95 L540 170 C450 190 360 150 260 185 C160 215 80 170 0 190 Z" fill="var(--aqua)"/>
    <path d="M0 125 C90 90 200 148 300 112 C390 82 470 118 540 102 L540 120 C450 135 360 120 260 150 C160 175 80 140 0 160 Z" fill="var(--foam)"/>
  </svg>
  <div class="brand" style="left:30px;top:28px">
    <span class="brand__mark"></span>
    <span class="brand__name">bayline<br>laundromat</span>
  </div>
  <div class="photo photo--couple" role="img" aria-label="Photo of a smiling couple holding a basket of laundry in front of washers"></div>
  <h1 class="headline">Fast forward<br>your<br>laundry day!</h1>
  <div class="burst burst--offer">
    <svg viewBox="0 0 100 100" aria-hidden="true"><polygon fill="var(--navy)" points="50,0 57,17 72,5 71,24 90,18 82,35 100,38 86,50 100,62 82,65 90,82 71,76 72,95 57,83 50,100 43,83 28,95 29,76 10,82 18,65 0,62 14,50 0,38 18,35 10,18 29,24 28,5 43,17"/></svg>
    <div class="burst__text"><span class="burst__big">50% off</span><span class="burst__small">on your first wash<br>and fold order<br>coupon valid</span></div>
  </div>
  <div class="bubble" style="left:195px;top:301px;width:136px;height:136px">
    <span class="bubble__title">Have large<br>laundry loads?</span>
    <span class="bubble__body">Bring them in your car<br>we have ample<br>parking space</span>
  </div>
  <div class="bubble" style="left:17px;top:365px;width:176px;height:176px">
    <span class="bubble__title bubble__title--red">Free wash</span>
    <span class="bubble__body bubble__body--large">One load of 20 lb wash<br>free with this<br>coupon valid</span>
  </div>
  <div class="photo photo--towels" role="img" aria-label="Photo of a man and woman holding stacks of folded towels in a laundromat"></div>
  <div class="bubble" style="left:83px;top:528px;width:156px;height:156px">
    <span class="bubble__title">No time for<br>grocery<br>shopping?</span>
    <span class="bubble__body">Do your grocery shopping<br>at nearby FreshMart while our<br>machines do your laundry</span>
  </div>
  <div class="call"><div class="call__label">CALL US</div><div class="call__phone">415-555-0148</div></div>
</section>

<section class="flyer flyer--back" aria-label="Flyer back">
  <svg class="flyer__sweep" viewBox="0 0 540 700" aria-hidden="true">
    <path d="M200 700 C260 520 400 400 540 330 L540 700 Z" fill="#36a0ea" opacity=".4"/>
    <path d="M0 300 C120 260 200 330 300 250 L300 700 L0 700 Z" fill="#1a3598" opacity=".35"/>
  </svg>
  <svg class="header-band" viewBox="0 0 540 210" aria-hidden="true">
    <rect width="540" height="120" fill="var(--navy)"/>
    <path d="M0 120 C90 80 200 140 300 105 C390 75 470 110 540 95 L540 170 C450 190 360 150 260 185 C160 215 80 170 0 190 Z" fill="var(--aqua)"/>
    <path d="M0 125 C90 90 200 148 300 112 C390 82 470 118 540 102 L540 120 C450 135 360 120 260 150 C160 175 80 140 0 160 Z" fill="var(--foam)"/>
  </svg>
  <div class="brand" style="left:252px;top:28px">
    <span class="brand__mark"></span>
    <span class="brand__name">bayline<br>laundromat</span>
  </div>
  <div class="photo--washer photo" style="border-radius:0;box-shadow:none" role="img" aria-label="Photo of a smiling woman holding a laundry basket beside a commercial washing machine"></div>
  <div class="bubble" style="left:25px;top:27px;width:166px;height:166px">
    <span class="bubble__title">Tired of<br>washing your<br>clothes in a dirty<br>laundromat?</span>
    <span class="bubble__body">We have the cleanest laundromat<br>in the bay area with efficient<br>attendants</span>
  </div>
  <div class="bubble" style="left:69px;top:209px;width:150px;height:150px">
    <span class="bubble__title">Hate doing<br>laundry?</span>
    <span class="bubble__body">We will fast forward your day<br>with our large commercial<br>washers and dryers. You<br>will be out of here in no time</span>
  </div>
  <div class="bubble" style="left:27px;top:364px;width:156px;height:156px">
    <span class="bubble__title">Get bored<br>doing laundry?</span>
    <span class="bubble__body">Not here! We have free wi-fi<br>and flat screen TV<br>to keep you<br>entertained</span>
  </div>
  <div class="bubble" style="left:180px;top:395px;width:150px;height:150px">
    <span class="bubble__title">No time for<br>laundry?</span>
    <span class="bubble__body">Bring it to us and collect<br>it washed, folded and<br>neatly packed after 24<br>hours</span>
  </div>
  <div class="bubble" style="left:25px;top:520px;width:160px;height:160px">
    <span class="bubble__title">Our location<br>is a multi<br>taskers dream</span>
    <span class="bubble__body">Grocery shopping at nearby FreshMart,<br>lunch at Golden Wok<br>(or Hero Sub or Cajun Chick'n)<br>coffee at Brewhouse Coffee</span>
  </div>
  <div class="burst burst--contact">
    <svg viewBox="0 0 278 190" preserveAspectRatio="none" aria-hidden="true"><polygon fill="var(--lime)" points="20,40 55,45 70,15 95,42 130,5 150,40 190,20 200,48 240,30 235,62 278,60 278,190 0,190 15,150 0,120 22,100 5,70"/></svg>
    <div class="burst__text">
      <span class="burst__title">BAYLINE LAUNDROMAT</span>
      <span class="burst__line">2280 Marlow St, San Francisco, CA 94115<br>(Next to FreshMart)<br>www.baylinelaundromat.com</span>
      <span class="burst__phone">CALL US: 415-555-0148</span>
      <span class="burst__line">Open every day from 6 am to 10 pm</span>
    </div>
  </div>
</section>

</body>
</html>
```